Business Card for Luxury Hospitality Industry Career Seeker

Need something Simple, Punctual, and Elegant.

Project goal is to update phone number, layout, and wording

I look forward to working with you to create a business card I can give to managers and employers in the Luxury Hospitality industry. I want to advance a career in this industry handing out cards to managers and directors on my way up.
Updates

Updated graphics preferences in brief - would like my name flanked by small Lion, Compass, & Rope and have the Halworth 5 Star logo on the back Added Saturday, January 14, 2017

Updated Brief:-Some wording has been removed-Card Front should be more simple and tidy now-Card Back word choice & flow is improved Added Sunday, January 15, 2017

Target Market(s)

Luxury Hospitality Industry Employers and Managers

Industry/Entity Type

Hospitality

Contact Information for Business Card

(Card Front)
Corbin T. Pellman (flanked by small Lion, Compass & Rope graphic)
Luxury Hospitality
555-317-8846
ridgefellow@mailvessel.example
netroster.example/in/corbin-pellman-vet-civ
My Experience = Our Success

(Card Back)
Graphic of: Halworth 5 Star logo and maybe QTR 5 Diamond Logo too
8 years military supply, logistics, & administrative experience
2 years intensive recruiting, marketing, and sales expertise
Adept problem solving, planning and management skills
5 Star, 5 Daimond, Luxury Hotels & Hospitality Rooms & Revenue

Requirements
Must have
• Name
• Phone Number
• Email Address
• Net Roster Address
• Slogan (My Experience = Our Success)
• Graphic on back: Halworth 5 Star logo
• Qualification Remarks
• Catchy logo
Nice to have
• Background that makes a viewer think Luxury Hospitality Experience and/or World Experience
• Color combinations I've seen & liked are black & yellow, black & white, and blue & white

```html
<!DOCTYPE html>
<html lang="en">
<head>
<meta charset="utf-8">
<title>Corbin T. Pellman – Business Card</title>
<link rel="stylesheet" href="https://fonts.googleapis.com/css2?family=Cinzel:wght@400;600&family=Montserrat:wght@700&display=swap">
<style>
  :root {
    --backdrop: #eeeeee;
    --card-black: #1c1c1c;
    --card-white: #ffffff;
    --band-grey: #8a8a8a;
    --accent-yellow: #f5ea14;
    --ink: #1a1a1a;
    --badge-gold: #c2a24a;
    --badge-blue: #2a5fae;
  }
  * { margin: 0; padding: 0; box-sizing: border-box; }
  html, body { width: 1200px; height: 799px; overflow: hidden; }
  body { background: var(--backdrop); position: relative; font-family: "Cinzel", serif; }

  .card { position: absolute; width: 607px; height: 348px; overflow: hidden; }

  /* Front (sits above the back card) */
  .card-front { left: 67px; top: 53px; background: var(--card-black); color: #fff; z-index: 2; }
  .front-mark {
    position: absolute; top: 42px; left: 0; width: 100%; text-align: center;
    color: var(--accent-yellow); font-size: 13px; font-weight: 600; letter-spacing: 1px;
  }
  .holder-name {
    position: absolute; top: 108px; left: 0; width: 100%; text-align: center;
    font-size: 41px; font-weight: 400; letter-spacing: 0.5px; line-height: 1;
  }
  .holder-role {
    position: absolute; top: 168px; left: 0; width: 100%; text-align: center;
    color: var(--accent-yellow); font-size: 24px; line-height: 1;
  }
  .holder-employer {
    position: absolute; top: 194px; left: 0; width: 100%; text-align: center;
    color: var(--accent-yellow); font-size: 15px; line-height: 1;
  }
  .contact-list { position: absolute; top: 245px; left: 0; width: 100%; font-size: 12.5px; font-weight: 600; }
  .contact-row { display: flex; justify-content: center; align-items: center; gap: 18px; height: 25px; }
  .contact-item { display: flex; align-items: center; gap: 7px; }
  .contact-icon { width: 17px; height: 17px; display: block; }
  .front-band { position: absolute; left: 0; bottom: 0; width: 607px; height: 66px; }
  .slogan {
    position: absolute; bottom: 15px; left: 0; width: 100%; text-align: center;
    font-family: "Montserrat", sans-serif; font-weight: 700; font-size: 12.5px;
    letter-spacing: 4.5px; text-transform: uppercase; color: var(--ink);
  }

  /* Back */
  .card-back { left: 526px; top: 320px; background: var(--card-white); color: var(--ink); z-index: 1; }
  .back-mark {
    position: absolute; top: 52px; left: 0; width: 100%; text-align: center;
    font-size: 13px; font-weight: 600; letter-spacing: 1px;
  }
  .rule { position: absolute; left: 40px; width: 540px; height: 12px; }
  .rule-top { top: 109px; }
  .rule-bottom { top: 212px; }
  .qualifications { position: absolute; top: 125px; left: 0; width: 100%; list-style: none; text-align: center; }
  .qualifications li { font-size: 12.5px; letter-spacing: 1.3px; line-height: 21.5px; }
  .badges { position: absolute; top: 236px; left: 0; width: 100%; display: flex; justify-content: center; gap: 48px; }
  .badge { width: 92px; height: 90px; display: block; }
</style>
</head>
<body>

<section class="card card-back">
  <div class="back-mark">Lion, Compass &amp; Rope</div>

  <svg class="rule rule-top" viewBox="0 0 540 12" aria-hidden="true">
    <line x1="10" y1="6" x2="530" y2="6" stroke="#1a1a1a" stroke-width="1.2"/>
    <path d="M0 6 L10 2 L10 10 Z M540 6 L530 2 L530 10 Z" fill="#1a1a1a"/>
  </svg>
  <ul class="qualifications">
    <li>8 years military supply, logistics &amp; administrative experience</li>
    <li>2 years intensive recruiting, marketing, and sales expertise</li>
    <li>Adept problem solving, planning and management skills</li>
    <li>5 star, 5 diamond, luxury hotels &amp; hospitality rooms &amp; revenue</li>
  </ul>
  <svg class="rule rule-bottom" viewBox="0 0 540 12" aria-hidden="true">
    <line x1="10" y1="6" x2="530" y2="6" stroke="#1a1a1a" stroke-width="1.2"/>
    <path d="M0 6 L10 2 L10 10 Z M540 6 L530 2 L530 10 Z" fill="#1a1a1a"/>
  </svg>

  <div class="badges">
    <svg class="badge" viewBox="0 0 92 90" role="img" aria-label="Halworth 5 Star award badge">
      <circle cx="46" cy="45" r="40" fill="var(--badge-gold)"/>
    </svg>
    <svg class="badge" viewBox="0 0 92 90" role="img" aria-label="QTR 5 Diamond award badge">
      <rect x="8" y="10" width="76" height="70" rx="6" fill="var(--badge-blue)"/>
    </svg>
  </div>
</section>

<section class="card card-front">
  <div class="front-mark">Lion, Compass &amp; Rope</div>
  <h1 class="holder-name">Corbin T. Pellman</h1>
  <p class="holder-role">Reservations Agent</p>
  <p class="holder-employer">Halworth 5 Star Luxury Hotel</p>

  <div class="contact-list">
    <div class="contact-row">
      <span class="contact-item">
        <svg class="contact-icon" viewBox="0 0 17 17" aria-hidden="true">
          <rect width="17" height="17" fill="var(--accent-yellow)"/>
          <rect x="3" y="4.5" width="11" height="8" fill="none" stroke="#1c1c1c" stroke-width="1.2"/>
          <path d="M3 4.5 L8.5 9.5 L14 4.5" fill="none" stroke="#1c1c1c" stroke-width="1.2"/>
        </svg>
        555-317-8846
      </span>
      <span class="contact-item">
        <svg class="contact-icon" viewBox="0 0 17 17" aria-hidden="true">
          <rect width="17" height="17" fill="var(--accent-yellow)"/>
          <path d="M5 3 L7.5 3 L8.3 6 L6.8 7.3 Q8 10 10 11 L11.4 9.6 L14 10.4 L14 13 Q13 14 11.5 14 Q5.5 13 3.5 5.5 Q3.5 4 5 3 Z" fill="#1c1c1c"/>
        </svg>
        ridgefellow@mailvessel.example
      </span>
    </div>
    <div class="contact-row">
      <span class="contact-item">
        <svg class="contact-icon" viewBox="0 0 17 17" aria-hidden="true">
          <rect width="17" height="17" fill="var(--accent-yellow)"/>
        </svg>
        netroster.example/in/corbin-pellman-vet-civ
      </span>
    </div>
  </div>

  <svg class="front-band" viewBox="0 0 607 66" preserveAspectRatio="none" aria-hidden="true">
    <path d="M0 0 Q303 42 607 0 L607 66 L0 66 Z" fill="var(--band-grey)"/>
    <path d="M0 0 Q303 42 607 0" fill="none" stroke="var(--accent-yellow)" stroke-width="3"/>
  </svg>
  <p class="slogan">My Experience = Our Success</p>
</section>

</body>
</html>
```